Quillfern Litigation Funding Letterhead & Document Template

We need a letter head designed for our fund. Our fund works with law firms and investors across the globe. We need a a cover letter template as well as a document template for subsequent pages. Blue and white color scheme is preferred. This is our predecessor's website: https://www.quillfernlc.com/index.html. Please see our logo attached. The logo color code is #19478d. Font is Gotham-Medium.
Target Market(s)
Sophisticated investors and law firms
Font styles to use
Sans Serif
Colors
0255a3

```html
<!DOCTYPE html>
<html lang="en">
<head>
<meta charset="utf-8">
<title>Quillfern Litigation Funding – Stationery &amp; Document Template</title>
<link href="https://fonts.googleapis.com/css2?family=Montserrat:wght@400;500;600;700&display=swap" rel="stylesheet">
<style>
  :root {
    --brand-blue: #0d4491;
    --backdrop: #dcdcdc;
    --paper: #ffffff;
    --body-text: #6b6b6b;
    --rule-dots: #0d4491;
  }
  * { box-sizing: border-box; margin: 0; padding: 0; }
  html, body { width: 1200px; height: 1200px; overflow: hidden; }
  body { background: var(--backdrop); font-family: "Montserrat", sans-serif; position: relative; }

  .page {
    position: absolute; width: 332px; height: 464px; background: var(--paper);
    box-shadow: 0 3px 6px rgba(0,0,0,.18); overflow: hidden;
  }
  .page--letterhead { left: 89px; top: 105px; }
  .page--cover { left: 446px; top: 105px; }
  .page--contact { left: 802px; top: 105px; }
  .page--toc { left: 89px; top: 633px; }
  .page--about { left: 446px; top: 633px; }
  .page--services { left: 802px; top: 633px; }

  .page__shapes { position: absolute; inset: 0; width: 100%; height: 100%; }

  /* wordmark */
  .wordmark { position: absolute; text-align: center; font-weight: 500; letter-spacing: .04em; text-transform: uppercase; line-height: 1.25; }
  .wordmark__square { display: block; margin: 0 auto 10px; width: 30px; height: 30px; }
  .wordmark--large { left: 0; width: 220px; top: 40px; font-size: 12.5px; }
  .wordmark--cover { left: 30px; color: var(--brand-blue); }
  .wordmark--cover .wordmark__square { background: var(--brand-blue); }
  .wordmark--contact { left: 14px; color: #fff; }
  .wordmark--contact .wordmark__square { background: #fff; }
  .wordmark--small { left: 22px; top: 26px; font-size: 6px; color: var(--brand-blue); text-align: left; display: flex; align-items: center; gap: 5px; }
  .wordmark--small .wordmark__square { margin: 0; width: 10px; height: 10px; background: var(--brand-blue); }

  /* letterhead contact */
  .sender { position: absolute; left: 219px; top: 25px; border-left: 1px solid var(--brand-blue); padding-left: 8px; font-size: 4.4px; line-height: 6.6px; color: #555; }
  .sender__name { color: var(--brand-blue); font-weight: 600; }
  .sender__row { display: flex; align-items: center; gap: 3px; }
  .icon { width: 4.5px; height: 4.5px; fill: var(--brand-blue); flex: none; }

  /* footer band */
  .footer-band { position: absolute; left: 0; top: 437px; width: 100%; height: 13px; background: var(--brand-blue); color: #fff; }
  .footer-band__url { position: absolute; left: 0; width: 345px; top: 0; line-height: 13px; text-align: center; font-size: 5.6px; letter-spacing: .18em; }
  .footer-band__mark { position: absolute; left: 289px; top: 3px; width: 7px; height: 7px; border: 1px solid #fff; }
  .footer-band__num { position: absolute; left: 314px; top: 0; line-height: 13px; font-size: 5px; font-weight: 700; }

  /* cover / contact titles */
  .cover-title { position: absolute; left: 157px; top: 318px; color: #fff; font-weight: 700; font-size: 19px; line-height: 24px; letter-spacing: .03em; }
  .cover-rule { position: absolute; left: 157px; width: 43px; height: 1.5px; }
  .cover-url { position: absolute; left: 157px; top: 412px; font-size: 7px; letter-spacing: .04em; }
  .page--cover .cover-rule { top: 400px; background: #fff; }
  .page--cover .cover-url { color: #fff; }

  .contact-title { position: absolute; left: 157px; top: 310px; color: var(--brand-blue); font-size: 19px; letter-spacing: .04em; font-weight: 400; }
  .contact-title strong { font-weight: 700; }
  .page--contact .cover-rule { background: var(--brand-blue); }
  .contact-list { position: absolute; left: 157px; top: 349px; font-size: 5.8px; line-height: 7.6px; color: #555; }
  .contact-list .sender__row { align-items: flex-start; }
  .contact-list .icon { margin-top: 1.5px; }
  .page--contact .cover-url { color: var(--brand-blue); }

  /* table of contents */
  .toc__header { position: absolute; left: 0; top: 0; width: 100%; height: 59px; background: var(--brand-blue); color: #fff; font-weight: 700; font-size: 15px; letter-spacing: .03em; text-align: center; line-height: 62px; }
  .toc__list { position: absolute; left: 34px; top: 92px; width: 265px; list-style: none; }
  .toc__item { display: flex; justify-content: space-between; height: 26.4px; padding-top: 4px; border-bottom: 1.2px dotted var(--rule-dots); color: var(--brand-blue); font-size: 10px; letter-spacing: .04em; }

  /* inner pages */
  .section-title { position: absolute; left: 26px; width: 280px; padding-bottom: 2px; border-bottom: .8px solid var(--brand-blue); color: var(--brand-blue); font-size: 10.5px; letter-spacing: .04em; font-weight: 400; }
  .section-title strong { font-weight: 700; }
  .section-title__mark { position: absolute; right: 0; top: 1px; width: 8px; height: 8px; border: 1px solid var(--brand-blue); }
  .copy { position: absolute; font-size: 5.3px; line-height: 7.5px; color: var(--body-text); text-align: justify; }
  .copy p + p { margin-top: 7px; }
  .copy b { color: var(--brand-blue); font-weight: 700; }
  .photo-slot { position: absolute; background: linear-gradient(110deg, #cfcfcf 0%, #f4f4f4 40%, #e6e6e6 65%, #c8c8c8 100%); border: .5px solid #d6d6d6; }

  .service { position: absolute; width: 131px; font-size: 5.3px; line-height: 7.5px; color: var(--body-text); text-align: justify; }
  .service__num { float: left; width: 14px; height: 10px; margin: 1px 4px 0 0; background: var(--brand-blue); color: #fff; font-weight: 700; font-size: 5.5px; line-height: 10px; text-align: center; }
</style>
</head>
<body>

<!-- Letterhead -->
<section class="page page--letterhead">
  <div class="wordmark wordmark--small"><span class="wordmark__square"></span>Quillfern Litigation Funding</div>
  <address class="sender" style="font-style:normal">
    <div class="sender__name">Quillfern Litigation Funding</div>
    <div>412 Harbor View Road</div>
    <div>Juneau, Alaska 99801</div>
    <div class="sender__row"><svg class="icon" viewBox="0 0 10 10"><path d="M2 0.5l2 2-1 1.2c.6 1.3 1.5 2.2 2.8 2.8l1.2-1 2 2-1.4 1.8C4 9 1 6 0.3 1.9z"/></svg>555-014-2288</div>
    <div class="sender__row"><svg class="icon" viewBox="0 0 10 10"><rect x="0" y="2" width="10" height="6.5"/></svg>info@quillfernlc.com</div>
  </address>
  <footer class="footer-band">
    <span class="footer-band__url">WWW.QUILLFERNLC.COM</span>
    <span class="footer-band__mark"></span>
  </footer>
</section>

<!-- Cover -->
<section class="page page--cover">
  <svg class="page__shapes" viewBox="0 0 332 464" preserveAspectRatio="none">
    <polygon points="0,0 55,0 0,78" fill="var(--brand-blue)"/>
    <polygon points="332,0 332,464 0,464" fill="var(--brand-blue)"/>
  </svg>
  <div class="wordmark wordmark--large wordmark--cover"><span class="wordmark__square"></span>Quillfern Litigation<br>Funding</div>
  <h1 class="cover-title">COMPANY<br>PROJECT<br>PROPOSAL</h1>
  <div class="cover-rule"></div>
  <div class="cover-url">QUILLFERNLC.COM</div>
</section>

<!-- Contact -->
<section class="page page--contact">
  <svg class="page__shapes" viewBox="0 0 332 464" preserveAspectRatio="none">
    <polygon points="0,0 329,0 0,464" fill="var(--brand-blue)"/>
    <polygon points="332,404 332,464 289,464" fill="var(--brand-blue)"/>
  </svg>
  <div class="wordmark wordmark--large wordmark--contact"><span class="wordmark__square"></span>Quillfern Litigation<br>Funding</div>
  <h2 class="contact-title"><strong>CONTACT</strong> US</h2>
  <div class="cover-rule" style="top:340px"></div>
  <address class="contact-list" style="font-style:normal">
    <div class="sender__row"><svg class="icon" viewBox="0 0 10 10"><path d="M5 0a3.5 3.5 0 0 1 3.5 3.5C8.5 6 5 10 5 10S1.5 6 1.5 3.5A3.5 3.5 0 0 1 5 0z"/></svg><span>Quillfern Litigation Funding<br>412 Harbor View Road<br>Juneau, Alaska 99801</span></div>
    <div class="sender__row"><svg class="icon" viewBox="0 0 10 10"><path d="M2 0.5l2 2-1 1.2c.6 1.3 1.5 2.2 2.8 2.8l1.2-1 2 2-1.4 1.8C4 9 1 6 0.3 1.9z"/></svg>555-014-2288</div>
    <div class="sender__row"><svg class="icon" viewBox="0 0 10 10"><rect x="0" y="2" width="10" height="6.5"/></svg>info@quillfernlc.com</div>
  </address>
  <div class="cover-rule" style="top:400px"></div>
  <div class="cover-url">QUILLFERNLC.COM</div>
</section>

<!-- Table of contents -->
<section class="page page--toc">
  <h2 class="toc__header">TABLE OF CONTENTS</h2>
  <ol class="toc__list">
    <li class="toc__item"><span>About Us</span><span>04</span></li>
    <li class="toc__item"><span>Our Poprtfolio</span><span>05</span></li>
    <li class="toc__item"><span>Our Services</span><span>06</span></li>
    <li class="toc__item"><span>Mission &amp; Vission</span><span>07</span></li>
    <li class="toc__item"><span>Our Team</span><span>08</span></li>
    <li class="toc__item"><span>Case Study</span><span>09</span></li>
    <li class="toc__item"><span>Our Company</span><span>10</span></li>
    <li class="toc__item"><span>Our Professional Group</span><span>11</span></li>
    <li class="toc__item"><span>Our Projects</span><span>12</span></li>
    <li class="toc__item"><span>Global Market</span><span>13</span></li>
    <li class="toc__item"><span>How We Works</span><span>14</span></li>
    <li class="toc__item" style="border-bottom:none"><span>Why Choose US</span><span>15</span></li>
  </ol>
  <footer class="footer-band">
    <span class="footer-band__url">WWW.QUILLFERNLC.COM</span>
    <span class="footer-band__mark"></span>
    <span class="footer-band__num">1</span>
  </footer>
</section>

<!-- About / Portfolio -->
<section class="page page--about">
  <h2 class="section-title" style="top:20px"><strong>ABOUT</strong> US<span class="section-title__mark"></span></h2>
  <div class="copy" style="left:26px;top:41px;width:280px">
    <p>We provide capital to law firms and claimants pursuing strong commercial cases, allowing meritorious disputes to reach resolution without straining operating budgets. Our team reviews each matter with care, weighing legal merit, recoverability and timing before committing funds. Investors gain access to an uncorrelated asset class managed with discipline, transparency and clear reporting at every stage. Since our founding we have partnered with firms across many jurisdictions and practice areas.</p>
  </div>
  <div class="photo-slot" role="img" aria-label="Photograph of the firm's office or team" style="left:26px;top:103px;width:280px;height:103px"></div>

  <h2 class="section-title" style="top:219px"><strong>OUR</strong> POPRTFOLIO<span class="section-title__mark"></span></h2>
  <div class="copy" style="left:26px;top:240px;width:139px">
    <p>Over the past decade we have funded disputes in construction, energy, intellectual property, insolvency and international trade. Our portfolio spans courts and arbitral seats on several continents, and our outcomes reflect careful selection and close collaboration with experienced counsel. We measure success by results for clients and steady, responsible returns for our investors.</p>
    <p>Every matter passes through a staged review covering merits, damages, enforcement and budget before any capital is committed to the case.</p>
    <p>Recent highlights are listed on the following pages.</p>
  </div>
  <div class="copy" style="left:179px;top:240px;width:127px">
    <p>Our investment committee brings together former litigators, arbitrators and finance professionals who assess risk from every angle. This depth of experience lets us move quickly on urgent matters while keeping our standards high.</p>
  </div>
  <div class="photo-slot" role="img" aria-label="Photograph illustrating a portfolio case" style="left:179px;top:331px;width:127px;height:85px"></div>

  <footer class="footer-band">
    <span class="footer-band__url">WWW.QUILLFERNLC.COM</span>
    <span class="footer-band__mark"></span>
    <span class="footer-band__num">2</span>
  </footer>
</section>

<!-- Services / Mission -->
<section class="page page--services">
  <h2 class="section-title" style="top:20px"><strong>OUR</strong> SERVICES<span class="section-title__mark"></span></h2>
  <div class="copy" style="left:26px;top:41px;width:280px">
    <p>Our services cover single case funding, portfolio facilities for law firms, and monetisation of judgments and awards. Each structure is tailored to the needs of the client and the profile of the claim. We work alongside counsel from first assessment through settlement, offering practical support while leaving strategy and control of the case with the legal team.</p>
  </div>
  <div class="service" style="left:28px;top:106px"><span class="service__num">1</span>Single case funding for commercial claims, covering legal fees, expert costs and disbursements so that firms can pursue strong matters with confidence and steady cash flow.</div>
  <div class="service" style="left:176px;top:105px"><span class="service__num">2</span>Portfolio facilities that spread risk across several cases, giving law firms flexible capital to grow their practice and take on larger disputes over time.</div>
  <div class="service" style="left:28px;top:163px"><span class="service__num">3</span>Monetisation of judgments and arbitral awards, turning a favourable ruling into working capital while enforcement continues in the background under expert guidance.</div>
  <div class="service" style="left:176px;top:162px"><span class="service__num">4</span>Adverse cost cover and insurance arrangements that protect claimants from downside exposure and allow settlement talks to proceed on a balanced footing.</div>

  <h2 class="section-title" style="top:219px"><strong>MISSION &amp;</strong> VISSION<span class="section-title__mark"></span></h2>
  <div class="copy" style="left:26px;top:240px;width:134px">
    <p><b>Mission</b> : To give deserving claims the resources they need, supporting law firms with fair, flexible capital and helping clients secure the outcomes the law intends. We aim to make access to justice less dependent on the size of a balance sheet, acting with integrity and clarity in every partnership we form.</p>
    <p>We hold ourselves to clear standards of conduct and review our work regularly, so that clients and investors can rely on us over the long term.</p>
  </div>
  <div class="copy" style="left:172px;top:240px;width:134px">
    <p><b>Vission</b> : To be the most trusted partner in litigation finance, known to law firms and investors for sound judgement, open communication and consistent results. We see a market where funding is transparent, fairly priced and available to any party with a strong case, wherever the dispute is heard.</p>
    <p>Our growth will follow the success of our partners, built one carefully chosen matter at a time across the markets we serve.</p>
  </div>

  <footer class="footer-band">
    <span class="footer-band__url">WWW.QUILLFERNLC.COM</span>
    <span class="footer-band__mark"></span>
    <span class="footer-band__num">3</span>
  </footer>
</section>

</body>
</html>
```